Rack Card for Bright Oak Dog Training

I love the logo you designed for me a while back (I had it updated and have the new files).

I need a rack card designed, 2 sided.

One side will be Bright Oak Dog Training (my general dog training business)

The other side will be my Deaf and Blind Dog Training Business speciality.

Both sides Full Color/4 color

3.5 x 8.5 inches

I can provide photos and text accordingly.

Let me know the estimated price and Turn around time.

```html
<!DOCTYPE html>
<html lang="en">
<head>
<meta charset="utf-8">
<title>Bright Oak Dog Training – Rack Card</title>
<link href="https://fonts.googleapis.com/css2?family=Poppins:wght@400;600;700;800&family=Oswald:wght@600&display=swap" rel="stylesheet">
<style>
:root{
  --orange:#e0962a;
  --orange-soft:#c9843f;
  --charcoal:#2b2b2b;
  --ink:#1e1e1e;
  --white:#ffffff;
  --stage:#eeeeee;
  --ring:#b9b9b9;
  --beige:#f1dcbc;
}
*{margin:0;padding:0;box-sizing:border-box}
html,body{width:691px;height:1200px;overflow:hidden;background:var(--stage)}
body{position:relative;font-family:"Poppins",sans-serif;color:var(--ink)}
.card{position:absolute;top:223px;width:310px;height:753px;background:var(--white);overflow:hidden;box-shadow:0 4px 14px rgba(0,0,0,.18)}
.card--general{left:25px}
.card--special{left:356px}
.card svg.shapes{position:absolute;inset:0}
.abs{position:absolute}

/* general side */
.logo-badge{left:18px;top:174px;width:130px;height:130px;border-radius:50%;background:var(--ring);display:flex;align-items:center;justify-content:center}
.logo-badge span{width:112px;height:112px;border-radius:50%;background:var(--charcoal);display:flex;align-items:center;justify-content:center;text-align:center;color:var(--white);font-weight:600;font-size:15px;line-height:1.1}
.headline{left:0;width:310px;top:310px;text-align:center;line-height:1}
.headline .hl-orange{display:block;color:var(--orange);font-weight:800;font-size:22.5px;margin-bottom:1px}
.headline .hl-dark{display:block;color:var(--ink);font-weight:800;font-size:22px;margin-top:1px}
.headline .hl-light{display:block;color:var(--ink);font-weight:400;font-size:17.5px;margin-top:2px}
.section-title{font-weight:700;font-size:16px;line-height:1.1}
.section-title .accent{color:var(--orange);display:block}
.section-title .plain{color:var(--white);display:block}
.services{left:26px;top:514px;width:270px;display:grid;grid-template-columns:122px 140px;row-gap:10px;color:var(--white);font-size:10.8px;list-style:none}
.tick{position:relative;padding-left:15px;line-height:1.25}
.tick::before{content:"";position:absolute;left:0;top:3px;width:9px;height:9px;border-radius:50%;background:var(--orange)}
.tick::after{content:"";position:absolute;left:3px;top:4.6px;width:2.4px;height:4px;border:solid var(--white);border-width:0 1.2px 1.2px 0;transform:rotate(45deg)}
.tick--dark::before{background:var(--ink)}
.areas{left:20px;top:609px;width:280px;color:var(--orange);font-weight:700;font-size:10px;line-height:1.3}
.cta{left:22px;top:646px;width:264px;height:37px;background:var(--orange);color:var(--white);font-weight:800;font-size:12.6px;line-height:1.05;text-align:center;display:flex;align-items:center;justify-content:center}
.contact{left:21px;top:693px;width:270px;display:flex;align-items:flex-start;color:var(--white)}
.contact .name{color:var(--orange);font-weight:700;font-size:10px;line-height:1.05;width:66px;padding-top:2px}
.contact .office{font-size:8.6px;line-height:1.2}
.contact .office b{display:flex;align-items:center;gap:3px;font-size:10px;font-weight:600}
.contact .office b i{width:8px;height:8px;border-radius:50%;background:var(--orange);display:inline-block}
.contact .divider{width:1px;height:22px;background:#777;margin:0 9px 0 11px}
.web{left:0;width:310px;top:722px;text-align:center;color:var(--white);font-size:10px;letter-spacing:1.1px}
.web em{font-style:normal;color:var(--orange)}

/* special side */
.kicker{left:0;width:310px;top:21px;text-align:center;color:var(--orange);font-weight:800;font-size:15.5px;letter-spacing:1.6px}
.title{left:0;width:310px;top:39px;text-align:center;font-family:"Oswald",sans-serif;font-weight:600;font-size:21px;letter-spacing:-.2px;color:var(--ink);transform:scaleY(1.15)}
.deaf-title{left:61px;top:118px;font-weight:700;font-size:17px;color:var(--ink)}
.deaf-list{left:62px;top:147px;width:226px;list-style:none;font-size:9.6px;color:var(--white);line-height:1.22}
.deaf-list li{margin-bottom:11px}
.blind-title{left:21px;top:416px}
.blind-list{left:24px;top:471px;width:262px;list-style:none;font-size:9.6px;color:var(--white);line-height:1.22}
.blind-list li{margin-bottom:11px}
</style>
</head>
<body>

<!-- General training side -->
<section class="card card--general">
  <svg class="shapes" width="310" height="753" viewBox="0 0 310 753">
    <defs>
      <linearGradient id="pupTone" x1="0" y1="0" x2="0" y2="1">
        <stop offset="0" stop-color="#c47a3a"/>
        <stop offset="1" stop-color="#e9d7c0"/>
      </linearGradient>
    </defs>
    <path d="M108 0 A152 152 0 0 0 180 288" fill="none" stroke="var(--orange)" stroke-width="1"/>
    <path d="M96 12 A160 160 0 0 0 150 268" fill="none" stroke="var(--ink)" stroke-width="1"/>
    <g role="img" aria-label="Photo of a happy spaniel with its mouth open on an orange backdrop">
      <circle cx="190" cy="118" r="152" fill="var(--orange)"/>
    </g>
    <path d="M115 268 Q220 300 310 232" fill="none" stroke="var(--orange)" stroke-width="1"/>
    <path d="M0 450 Q110 400 240 455 T310 540" fill="none" stroke="var(--orange)" stroke-width="1.2"/>
    <path d="M0 458 Q110 410 240 462 T310 560 L310 753 L0 753 Z" fill="var(--charcoal)"/>
    <g role="img" aria-label="Photo of a small red and white dog raising a paw">
      <rect x="214" y="400" width="86" height="98" rx="38" fill="url(#pupTone)"/>
    </g>
  </svg>
  <div class="abs logo-badge"><span>Bright<br>Oak</span></div>
  <h1 class="abs headline">
    <span class="hl-orange">HAVING A HAPPY &amp;</span>
    <span class="hl-orange">WELL-BALANCED</span>
    <span class="hl-dark">DOG IS ONE OF LIFE’S</span>
    <span class="hl-light">GREATEST PLEASURES!</span>
  </h1>
  <h2 class="abs section-title" style="left:22px;top:463px"><span class="accent">Services</span><span class="plain">We Provide</span></h2>
  <ul class="abs services">
    <li class="tick">Puppy Training</li><li class="tick">Rescue Dog Training</li>
    <li class="tick">House Breaking</li><li class="tick">Separation Anxiety</li>
    <li class="tick">Leash Training</li><li class="tick">Socialization</li>
    <li class="tick">Obedience</li><li class="tick">Behavioral issues</li>
  </ul>
  <p class="abs areas">Private Dog Trainer for Orange County, South Bay, Long Beach, Venice Beach and West Los Angeles</p>
  <div class="abs cta">SCHEDULE FREE 15 MINUTE PHONE<br>CONSULTATION</div>
  <div class="abs contact">
    <div class="name">DANA<br>WHITLEY</div>
    <div class="office">LOS ANGELES<b><i></i>(555) 201-4830</b></div>
    <div class="divider"></div>
    <div class="office">ORANGE COUNTY<b><i></i>(555) 309-7742</b></div>
  </div>
  <p class="abs web">www.<em>brightoakdogtraining</em>.com</p>
</section>

<!-- Deaf and blind speciality side -->
<section class="card card--special">
  <svg class="shapes" width="310" height="753" viewBox="0 0 310 753">
    <path d="M2 320 A158 158 0 0 1 300 150" fill="none" stroke="var(--ink)" stroke-width="1"/>
    <circle cx="162" cy="235" r="153" fill="var(--orange)"/>
    <path d="M0 351 Q160 318 250 420 Q300 480 310 540 L310 677 L282 753 L0 753 Z" fill="var(--charcoal)"/>
    <path d="M230 410 Q300 480 310 560" fill="none" stroke="var(--orange)" stroke-width="1"/>
    <path d="M310 660 L270 753" stroke="var(--orange)" stroke-width="1.2"/>
    <circle cx="212" cy="362" r="88" fill="var(--beige)"/>
    <g role="img" aria-label="Photo of a person giving a hand signal to a black and white dog on grass">
      <circle cx="89" cy="348" r="64" fill="#b98a4a"/>
      <circle cx="89" cy="348" r="60" fill="#5f7a3c"/>
    </g>
    <g role="img" aria-label="Photo of a smiling merle shepherd dog outdoors">
      <circle cx="212" cy="362" r="83" fill="#b7a58e"/>
    </g>
  </svg>
  <p class="abs kicker">WE SPECIALIZE IN</p>
  <h1 class="abs title">DEAF AND BLIND DOG TRAINING</h1>
  <h2 class="abs deaf-title">Deaf Dog Training</h2>
  <ul class="abs deaf-list">
    <li class="tick tick--dark">Deaf dogs can easily be trained using hand signals.</li>
    <li class="tick tick--dark">We owe it to our dogs to teach them how to behave, and that the world is a safe place.</li>
    <li class="tick tick--dark">A dog with special needs is no exception.</li>
    <li class="tick tick--dark">Training a dog that is deaf can come with it challenges.</li>
  </ul>
  <h2 class="abs section-title blind-title"><span class="accent">Blind Dog</span><span class="plain">Training</span></h2>
  <ul class="abs blind-list">
    <li class="tick">Deaf dogs can easily be trained using sound signals.</li>
    <li class="tick">We owe it to our dogs to teach them how to behave, to know their surrounding even with their sight is loss, and that the world is a safe place.</li>
    <li class="tick">A dog with special needs is no exception.</li>
    <li class="tick">Owners can wear a jingling bell, so your blind dog can find you.</li>
    <li class="tick">Blind Dogs have EXTREMELY heightened senses (especially smell and sound).</li>
  </ul>
  <div class="abs cta">SCHEDULE FREE 15 MINUTE PHONE<br>CONSULTATION</div>
  <div class="abs contact">
    <div class="name">DANA<br>WHITLEY</div>
    <div class="office">LOS ANGELES<b><i></i>(555) 201-4830</b></div>
    <div class="divider"></div>
    <div class="office">ORANGE COUNTY<b><i></i>(555) 309-7742</b></div>
  </div>
  <p class="abs web">www.<em>brightoakdogtraining</em>.com</p>
</section>

</body>
</html>
```